Feature Film "look book" digital brochure

Looking for a designer to create an edgy, gritty, eye popping visual representation of my film to get interest from investors, producers and actors. Basically it would introduce the project and in about 7-9 pages; give an overview of the film, why to invest, an artistic statement and potential casting ideas and an introduction to the key crew. I have included way more images than you would ever need in the files. I've also included samples for other films and a brochure someone already did for the film just to give you an idea of how it should be structured and the text content. Visually that piece is not a good guideline because it doesn't visually rep the film which is why I"m doing this contest!
The film is called 4 by 12: the sentence of an alcoholic teacher who commits a crime she can't remember and whose chance for survival depends on an ex-drug dealer and a basketball court.
Independent film investors, artists
Digital

```html
<!DOCTYPE html>
<html lang="en">
<head>
<meta charset="utf-8">
<title>Full Court — Synopsis</title>
<link rel="stylesheet" href="https://fonts.googleapis.com/css2?family=Stardos+Stencil:wght@700&family=Open+Sans:ital,wght@1,500&display=swap">
<style>
  :root {
    --asphalt: #2b2b2b;
    --asphalt-deep: #1c1c1c;
    --olive: #6f6544;
    --olive-faint: rgba(122, 112, 72, 0.55);
    --panel: rgba(242, 242, 244, 0.93);
    --ink: #151515;
    --white: #ffffff;
    --sky-top: #5d88c9;
    --sky-low: #b9cfe6;
    --grass: #7b8a3a;
  }
  html, body {
    margin: 0;
    padding: 0;
    overflow: hidden;
    background: var(--asphalt-deep);
  }
  .page {
    position: relative;
    width: 1200px;
    height: 848px;
    overflow: hidden;
    background: var(--asphalt);
  }
  .texture {
    position: absolute;
    inset: 0;
    width: 1200px;
    height: 848px;
  }
  .title-band {
    position: absolute;
    left: 0;
    top: 80px;
    width: 1200px;
    height: 146px;
    background: var(--olive);
    mix-blend-mode: normal;
    opacity: 0.92;
  }
  .ghost-title {
    position: absolute;
    left: 420px;
    top: 728px;
    margin: 0;
    font-family: "Stardos Stencil", "Georgia", serif;
    font-weight: 700;
    font-size: 150px;
    line-height: 1;
    letter-spacing: 4px;
    color: var(--olive-faint);
    white-space: nowrap;
  }
  .section-title {
    position: absolute;
    left: 48px;
    top: 52px;
    margin: 0;
    font-family: "Stardos Stencil", "Georgia", serif;
    font-weight: 700;
    font-size: 74px;
    line-height: 1;
    letter-spacing: 1px;
    color: var(--white);
  }
  .synopsis-panel {
    position: absolute;
    left: 50px;
    top: 141px;
    width: 555px;
    height: 662px;
    background: var(--panel);
    box-sizing: border-box;
    padding: 20px 22px 0 17px;
  }
  .synopsis-panel p {
    margin: 0 0 22px;
    font-family: "Open Sans", "Helvetica", sans-serif;
    font-style: italic;
    font-weight: 500;
    font-size: 16.6px;
    line-height: 22.2px;
    color: var(--ink);
  }
  .still-frame {
    position: absolute;
    left: 644px;
    top: 71px;
    width: 516px;
    height: 733px;
    box-sizing: border-box;
    border: 5px solid var(--white);
    background: var(--white);
  }
  .still {
    width: 100%;
    height: 100%;
    background: linear-gradient(180deg, var(--sky-top) 0%, var(--sky-low) 72%, var(--grass) 100%);
  }
</style>
</head>
<body>
  <main class="page">
    <svg class="texture" viewBox="0 0 1200 848" aria-hidden="true">
      <filter id="grit">
        <feTurbulence type="fractalNoise" baseFrequency="0.9" numOctaves="3" seed="4"/>
        <feColorMatrix values="0 0 0 0 0  0 0 0 0 0  0 0 0 0 0  0 0 0 -1.4 1.05"/>
      </filter>
      <rect width="1200" height="848" fill="#3a3a3a"/>
      <rect width="1200" height="848" filter="url(#grit)" opacity="0.6"/>
    </svg>

    <div class="title-band"></div>
    <p class="ghost-title" aria-hidden="true">FULL COURT</p>

    <h1 class="section-title">SYNOPSIS</h1>

    <section class="synopsis-panel">
      <p>&nbsp;Lorem ipsum dolor sit amet, consectetur adipiscing elit. Nam euismod dui mi, nec adipiscing risus vehicula mattis. Donec aliquet erat ut urna facilisis blandit. Sed quis eleifend magna. Integer dui est, vulputate ut ullamcorper fringilla, sodales nec sapien. In ac nulla eu ante facilisis cursus. Donec aliquet ipsum consectetur metus pellentesque, ac elementum diam vestibulum. Nunc et urna ut ipsum vestibulum ornare sed eget sapien. Maecenas id mi porta, fermentum nunc a, vehicula enim. Fusce adipiscing urna eu justo consequat, ac sollicitudin ipsum dictum.</p>
      <p>Donec eu elementum sem, pulvinar consectetur lacus. Aenean nunc dui, ornare id justo ut, porttitor imperdiet neque. Nulla magna dolor, malesuada ut tortor ut, convallis suscipit neque. Aliquam sed tincidunt orci, eu placerat elit. Vivamus quam augue, hendrerit id purus ut, porta dignissim sapien. Cras venenatis egestas mauris, quis sagittis quam consectetur at. Sed nec lacus eros. Cras sed molestie nisl. Phasellus bibendum lacinia placerat. Ut turpis mi, mollis ac gravida sed, ornare sollicitudin tortor. Aenean mauris ante, ultricies vitae nisi sit amet, rutrum faucibus turpis. Aenean gravida urna nec nisl dapibus pharetra. n</p>
    </section>

    <figure class="still-frame" style="margin:0">
      <div class="still" role="img" aria-label="Film still: a woman holding a basketball beneath an outdoor hoop on a public court, blue sky and chain-link fence behind"></div>
    </figure>
  </main>
</body>
</html>
```